Ridgeway Builders, Inc. Concrete cutting special flyer , 10% off for new customers

Flyer to send to potential customers and business associates and general contractors - specializing in Concrete-Flatwork
Concrete Repair
Concrete Sidewalks
Patios & Driveways
Stoops, Porches And Staircase
Foundation Contractors--Concrete
Facade Restoration
Concrete
Patios
Driveways
Walkways
Commercial Concrete Work
Concrete Restoration
Building Alterations
Foundations - Concrete
Concrete Repairs
rbwxpo.com

Target Market(s)

Homeowners, business owners & general contractors

Industry/Entity Type

Construction

Font styles to use
Serif

Colors
FFC000
F8CF3A
FAE287
FDF2CF
FEFAEE
EB3D1F
EC4F4E
F09395
F8D3D4
FCEDEE

Requirements
Must have
• General Contracting, masonry - Must have Logo Please see list of services Ridgeway Builders NY, Inc., has to offer. Concrete-Flatwork Concrete Repair Concrete Sidewalks Patios & Driveways Stoops, Porches And Staircase Foundation Contractors--Concrete Facade Restoration Concrete Patios Driveways Walkways Commercial Concrete Work Concrete Restoration Building Alterations Foundations - Concrete Concrete Repairs
Nice to have
• List of services - Logo - Black & Gold with a bold color to stand out (preferably reds)

```html
<!DOCTYPE html>
<html lang="en">
<head>
<meta charset="utf-8">
<title>Ridgeway Builders NY, Inc. — Services Flyer</title>
<link href="https://fonts.googleapis.com/css2?family=Open+Sans:wght@400;600;700&display=swap" rel="stylesheet">
<style>
  :root{
    --green:#1f3a26;
    --green-dark:#173020;
    --gold:#cda84b;
    --gold-text:#d4ac48;
    --paper:#ffffff;
    --bg:#6f6f6f;
    --ink:#3a3a3a;
    --photo-warm-a:#8a5a45;
    --photo-warm-b:#c79b74;
    --photo-site-a:#6d6a5a;
    --photo-site-b:#a8946a;
  }
  *{box-sizing:border-box;margin:0;padding:0}
  html,body{width:1200px;height:1074px;overflow:hidden}
  body{background:var(--bg);font-family:"Open Sans",Arial,sans-serif;position:relative}
  .flyer{position:absolute;left:232px;top:17px;width:735px;height:1040px;background:var(--paper);overflow:hidden}
  .brand{position:absolute;left:40px;top:38px;display:flex;align-items:center;gap:10px;color:var(--green);font-weight:700;font-size:22px;line-height:1.1}
  .brand-mark{width:16px;height:16px;background:var(--green)}
  .contact{position:absolute;right:40px;top:118px;text-align:right;font-weight:700;font-size:20px;line-height:1.3;color:var(--green)}
  .contact span{color:var(--gold-text)}
  .hero-photo{position:absolute;left:80px;top:100px;width:620px;height:460px;
    background:linear-gradient(120deg,var(--photo-warm-a),var(--photo-warm-b) 55%,#7a4a3a);
    clip-path:polygon(0 0,58% 0,58% 20%,100% 20%,100% 100%,0 100%)}
  .headline{position:absolute;left:40px;top:230px;width:390px;height:120px;background:var(--green);padding:14px 22px;color:#fff}
  .headline::before{content:"";position:absolute;left:0;top:-18px;border-right:40px solid #2c4f35;border-top:18px solid transparent}
  .headline h1{color:var(--gold-text);font-size:23px;font-weight:700;line-height:1.1;text-transform:uppercase}
  .headline p{font-size:12.5px;line-height:1.3;margin-top:6px}
  .services-title{position:absolute;left:40px;top:448px;width:350px;height:66px;background:var(--green);color:var(--gold-text);font-weight:700;font-size:38px;line-height:66px;padding-left:22px;text-transform:uppercase}
  .bottom-band{position:absolute;left:0;top:790px;width:430px;height:250px;background:var(--green)}
  .services{position:absolute;left:92px;top:514px;width:320px;height:460px;background:var(--gold);padding:14px 0 0 22px;list-style:none}
  .services li{position:relative;padding-left:24px;font-weight:700;font-size:17px;line-height:26.5px;color:var(--green);white-space:nowrap}
  .services li::before{content:"";position:absolute;left:0;top:7px;width:12px;height:12px;border:1.5px solid var(--green);border-radius:50%}
  .services li::after{content:"";position:absolute;left:4px;top:9px;width:3px;height:6px;border:solid var(--green);border-width:0 2px 2px 0;transform:rotate(40deg)}
  .website{position:absolute;left:40px;top:995px;color:#fff;font-size:20px;letter-spacing:9px;font-weight:600}
  .website span{color:var(--gold-text)}
  .website-rule{position:absolute;left:342px;top:1010px;width:88px;height:1px;background:#fff}
  .badge{position:absolute;left:470px;top:470px;width:180px;height:180px}
  .site-photo{position:absolute;left:440px;top:612px;width:260px;height:158px;background:linear-gradient(160deg,var(--photo-site-a),var(--photo-site-b))}
  .what{position:absolute;left:432px;top:778px;width:293px}
  .what h2,.why h2{font-size:26px;font-weight:700;line-height:1.2;color:var(--green);text-transform:uppercase}
  .what h2 span,.why h2 span{color:var(--gold-text)}
  .what p{font-size:11.5px;line-height:1.3;color:var(--ink);margin-top:4px}
  .why{position:absolute;left:430px;top:925px;width:305px;height:115px;background:var(--green);padding:8px 16px}
  .why h2{color:#fff;font-size:22px}
  .why p{font-size:11.5px;line-height:1.25;color:#fff;margin-top:2px}
</style>
</head>
<body>
<main class="flyer">
  <div class="brand"><div class="brand-mark"></div>Ridgeway Builders NY, Inc.</div>
  <div class="contact">Call or Text <span>555-301-4820</span><br>or <span>555-301-7736</span></div>
  <div class="hero-photo" role="img" aria-label="Photo of a builder in a plaid shirt holding a yellow hard hat, wearing a tool belt, in front of a brick wall"></div>
  <section class="headline">
    <h1>Excavation Concrete Structural</h1>
    <p>We'll Get The Job Done Rite The first Time!! NY'S Leading Excavation, Foundation, Waterproofing and Flat Roof Specialists</p>
  </section>
  <div class="bottom-band"></div>
  <h2 class="services-title">Our Services</h2>
  <ul class="services">
    <li>Concrete Flatwork</li>
    <li>Concrete Repair</li>
    <li>Concrete Sidewalks</li>
    <li>Patios &amp; Driveways</li>
    <li>Stoops, Porches And Staircase</li>
    <li>Foundation Contractors--Concrete</li>
    <li>Facade Restoration</li>
    <li>Concrete</li>
    <li>Patios</li>
    <li>Driveways</li>
    <li>Walkways</li>
    <li>Commercial Concrete Work</li>
    <li>Concrete Restoration</li>
    <li>Building Alterations</li>
    <li>Foundations - Concrete</li>
    <li>Concrete Repairs</li>
  </ul>
  <div class="website">www.<span>rbwxpo</span>.com</div>
  <div class="website-rule"></div>
  <div class="site-photo" role="img" aria-label="Photo of an excavator and skid steer on a cleared job site"></div>
  <svg class="badge" viewBox="0 0 180 180" aria-label="New customers 10% off">
    <circle cx="90" cy="90" r="76" fill="#1f3a26"/>
    <circle cx="90" cy="90" r="78" fill="none" stroke="#1f3a26" stroke-width="16" stroke-linecap="round" stroke-dasharray="0 16.3"/>
    <circle cx="90" cy="90" r="64" fill="none" stroke="#cda84b" stroke-width="2.5"/>
    <text x="90" y="58" text-anchor="middle" fill="#fff" font-family="Open Sans, sans-serif" font-size="16">New</text>
    <text x="90" y="77" text-anchor="middle" fill="#fff" font-family="Open Sans, sans-serif" font-size="16">Customers</text>
    <line x1="50" y1="84" x2="130" y2="84" stroke="#cda84b" stroke-width="1"/>
    <text x="90" y="118" text-anchor="middle" fill="#d4ac48" font-family="Open Sans, sans-serif" font-weight="700" font-size="40">10%</text>
    <line x1="50" y1="126" x2="130" y2="126" stroke="#cda84b" stroke-width="1"/>
    <text x="90" y="146" text-anchor="middle" fill="#fff" font-family="Open Sans, sans-serif" font-size="20">off</text>
  </svg>
  <section class="what">
    <h2>What <span>we do ?</span></h2>
    <p>Our projects include both Residential and Commercial construction and repairs/restorations. Occupied and fully operational job sites are never a problem. And we can also plan, manage, and build multi-phase jobs. we specialize in excavation, foundation, Roofing and waterproofing.</p>
  </section>
  <section class="why">
    <h2>Why <span>choose us?</span></h2>
    <p>We work with architects and designers to produce beautiful, functional structures. Call us today and bring our project management skills and extensive construction experience to your next project.</p>
  </section>
</main>
</body>
</html>
```